Redesign Colorful Business Card

Please redesign the card attached. It is too busy. Please don't eliminate any of the words. The repetivite word "free" can be used less often.

Target Market(s)

College Students.

Contact Information for Business Card

The details listed in the attached image

Font styles to use
Sans Serif

Requirements
Must have
• A clear and simple presentation and must be attractive.

```html
<!DOCTYPE html>
<html lang="en">
<head>
<meta charset="utf-8">
<title>StudyBright Business Card</title>
<link rel="stylesheet" href="https://fonts.googleapis.com/css2?family=Montserrat:wght@500;600;700;800;900&family=Oswald:wght@500;600&display=swap">
<style>
  :root {
    --green: #06402f;
    --red: #ec1c24;
    --yellow: #fdd10f;
    --yellow-deep: #f7a90d;
    --navy: #1b1f4d;
    --white: #ffffff;
    --page: #ffffff;
  }
  * { margin: 0; padding: 0; box-sizing: border-box; }
  html, body {
    width: 1200px; height: 1200px; overflow: hidden;
    background: var(--page);
    font-family: "Montserrat", Arial, sans-serif;
  }
  .card {
    position: absolute; left: 50px; top: 287px;
    width: 1100px; height: 626px;
    background: var(--green);
    overflow: hidden;
  }
  .brand-panel {
    position: absolute; left: 0; top: 24px;
    width: 447px; height: 304px;
    background: var(--red);
    border-radius: 0 30px 30px 0;
  }
  .brand-line {
    position: absolute; left: 0; width: 392px; top: 246px;
    display: flex; align-items: center; justify-content: center; gap: 12px;
    white-space: nowrap;
  }
  .brand-mark { width: 18px; height: 18px; background: var(--yellow); }
  .brand-name {
    color: var(--white); font-weight: 700; font-size: 29px; letter-spacing: 0.5px; line-height: 1;
  }
  .free-badge {
    position: absolute; left: 412px; top: 108px;
    width: 262px; height: 150px;
    background: linear-gradient(160deg, var(--yellow) 0%, var(--yellow-deep) 100%);
    border-radius: 14px;
    transform: rotate(-8deg);
    color: var(--navy);
    font-weight: 900;
    display: flex; flex-direction: column; align-items: center; justify-content: center;
    line-height: 1;
  }
  .free-badge .free-small { font-size: 24px; margin-right: 60px; transform: rotate(-14deg); }
  .free-badge .free-large { font-size: 60px; transform: rotate(-10deg); margin: 4px 0; }
  .free-badge .free-tail { font-size: 24px; margin-left: 80px; transform: rotate(-6deg); }
  .megaphone {
    position: absolute; left: 384px; top: 212px;
    width: 64px; height: 72px;
    border-radius: 10px;
    background: linear-gradient(135deg, #c9cbe8 0%, #5a63b8 100%);
  }
  .offer-kicker {
    position: absolute; left: 748px; top: 58px; width: 294px;
    font-family: "Oswald", "Arial Narrow", sans-serif; font-weight: 500;
    color: var(--white); font-size: 47px; line-height: 1; letter-spacing: -0.5px;
    white-space: nowrap; padding-bottom: 8px; border-bottom: 3px solid var(--white);
  }
  .offer-down {
    position: absolute; left: 748px; top: 130px;
    color: var(--yellow); font-weight: 900; font-size: 50px; line-height: 1;
    letter-spacing: 0.5px; white-space: nowrap;
  }
  .upto {
    position: absolute; left: 753px; top: 196px;
    width: 94px; height: 91px; background: var(--white); border-radius: 16px;
    color: var(--green); font-weight: 600; font-size: 38px; line-height: 0.95;
    display: flex; flex-direction: column; align-items: center; justify-content: center;
  }
  .percent {
    position: absolute; left: 866px; top: 190px;
    font-family: "Oswald", "Arial Narrow", sans-serif; font-weight: 600;
    color: var(--yellow); font-size: 104px; line-height: 1; white-space: nowrap;
  }
  .benefit {
    position: absolute; top: 372px; line-height: 51px;
    text-transform: uppercase; white-space: nowrap;
  }
  .benefit .plain { color: var(--white); font-weight: 500; font-size: 43px; display: block; }
  .benefit .strong { color: var(--yellow); font-weight: 800; font-size: 48px; display: block; }
  .benefit-class { left: 60px; }
  .benefit-memory { left: 602px; }
  .benefit-divider {
    position: absolute; left: 569px; top: 379px; width: 3px; height: 142px; background: var(--white);
  }
  .footer {
    position: absolute; left: 0; bottom: 0; width: 100%; height: 69px;
    background: var(--red);
    color: var(--white); font-weight: 600; font-size: 24px; white-space: nowrap;
    display: flex; align-items: center; padding-left: 60px;
  }
  .portrait {
    position: absolute; left: 866px; top: 326px; width: 234px; height: 300px;
    background: linear-gradient(180deg, #d9a98b 0%, #c78f6f 45%, #f2c744 60%, #eab935 100%);
    border-radius: 110px 110px 0 0;
  }
</style>
</head>
<body>
  <main class="card">
    <section class="brand-panel">
      <div class="brand-line">
        <span class="brand-mark"></span>
        <span class="brand-name">STUDYBRIGHT.COM</span>
      </div>
    </section>

    <div class="free-badge">
      <span class="free-small">FREE</span>
      <span class="free-large">FREE</span>
      <span class="free-tail">FREE</span>
    </div>
    <div class="megaphone" role="img" aria-label="Megaphone illustration announcing the free offer"></div>

    <div class="offer-kicker">CUT STUDY TIME</div>
    <div class="offer-down">DOWN BY</div>
    <div class="upto"><span>UP</span><span>TO</span></div>
    <div class="percent">50%</div>

    <p class="benefit benefit-class">
      <span class="plain">Learn a subject</span>
      <span class="strong">Without having</span>
      <span class="strong">to go to class</span>
    </p>
    <div class="benefit-divider"></div>
    <p class="benefit benefit-memory">
      <span class="plain">Memorize</span>
      <span class="plain">anything</span>
      <span class="strong">Quickly</span>
    </p>

    <footer class="footer">Copyright brightway services, LLC 2013-22 all rights reserved</footer>

    <div class="portrait" role="img" aria-label="Photo of an excited young woman in a yellow sweater whispering behind her hand"></div>
  </main>
</body>
</html>
```